R Snow Artist Business Card

I need a business card for myself working as an emerging artist. I have an artwork that has been exhibited at an Awards exhibition that I would like incorporated into my business card. The card needs to be simple but different so I was thinking about one that is perhaps half or 1/3 of the normal business card size so that it could be slipped comfortably into little pouches. I only want my name, email, mobile number and facebook artist page link on the card.Perhaps the artwork on the size of a normal business card and then the card chopped up into 3 so that I have 3 business cards of different look and my details on the blank side of the card..unless someone can come up with a more interesting concept that is simple and fit for an emerging artist :)

```html
<!DOCTYPE html>
<html lang="en">
<head>
<meta charset="utf-8">
<title>R Snow – Artist Cards</title>
<link rel="stylesheet" href="https://fonts.googleapis.com/css2?family=PT+Sans:wght@400;700&family=Dancing+Script:wght@400&display=swap">
<style>
  :root {
    --page: #ecebe8;
    --card-black: #050505;
    --card-red: #8e1309;
    --ink-white: #ffffff;
    --art-red: #d9321a;
    --art-deep: #a3160c;
    --art-orange: #ef7a1e;
    --art-yellow: #f3c83c;
    --card-w: 900px;
    --card-h: 250px;
  }
  * { margin: 0; padding: 0; box-sizing: border-box; }
  html, body {
    width: 1200px;
    height: 955px;
    overflow: hidden;
    background: var(--page);
  }
  .sheet {
    position: relative;
    width: 1200px;
    height: 955px;
  }
  .card {
    position: absolute;
    left: 150px;
    width: var(--card-w);
    height: var(--card-h);
    overflow: hidden;
    box-shadow: 0 6px 14px rgba(0, 0, 0, 0.18);
  }
  .card--details { top: 197px; background: var(--card-black); }
  .card--artwork { top: 507px; }

  .card__wedge {
    position: absolute;
    inset: 0;
    width: 100%;
    height: 100%;
  }
  .card__wedge path { fill: var(--card-red); }

  .details {
    position: absolute;
    inset: 0;
    color: var(--ink-white);
    font-family: "PT Sans", sans-serif;
  }
  .details__name {
    position: absolute;
    left: 0;
    right: 70px;
    top: 14px;
    text-align: center;
    font-weight: 700;
    font-size: 74px;
    letter-spacing: 1px;
    line-height: 1;
  }
  .details__phone {
    position: absolute;
    left: 0;
    right: 100px;
    top: 100px;
    text-align: center;
    font-weight: 700;
    font-size: 46px;
    letter-spacing: 2px;
    line-height: 1;
  }
  .details__web {
    position: absolute;
    left: 60px;
    right: 30px;
    top: 182px;
    text-align: center;
    font-weight: 400;
    font-size: 29px;
    letter-spacing: 0.8px;
    line-height: 1;
  }

  .artwork {
    position: absolute;
    inset: 0;
    background:
      radial-gradient(ellipse 30% 60% at 92% 25%, var(--art-yellow), transparent 70%),
      radial-gradient(ellipse 40% 70% at 15% 80%, var(--art-orange), transparent 70%),
      radial-gradient(ellipse 50% 60% at 55% 45%, var(--art-deep), transparent 75%),
      linear-gradient(100deg, var(--art-red) 0%, var(--art-orange) 45%, var(--art-red) 75%, var(--art-orange) 100%);
  }
  .artwork__signature {
    position: absolute;
    right: 28px;
    top: 128px;
    color: var(--ink-white);
    font-family: "Dancing Script", cursive;
    font-size: 52px;
    line-height: 1;
  }
</style>
</head>
<body>
  <main class="sheet">
    <section class="card card--details" aria-label="Contact side">
      <svg class="card__wedge" viewBox="0 0 900 250" preserveAspectRatio="none" aria-hidden="true">
        <path d="M0,250 C180,205 330,150 520,110 C680,78 800,68 900,62 L900,250 Z"/>
      </svg>
      <div class="details">
        <h1 class="details__name">R Snow</h1>
        <p class="details__phone">021 480317</p>
        <p class="details__web">artbook.net/pages/Rsnowartist/2097365180447312</p>
      </div>
    </section>

    <section class="card card--artwork" aria-label="Artwork side">
      <div class="artwork" role="img" aria-label="Abstract painting of red and orange foliage crossed by dark branches, with touches of yellow light and white blossom"></div>
      <span class="artwork__signature">snow</span>
    </section>
  </main>
</body>
</html>
```